Criação de Logo e Papelaria (6 itens) para Reabilitaçao Oral/Periodontia/Implantodontia com credenciamento em cirurgia guiada por computador.
" Profissional liberal: cirurgiao- dentista especialista em periodontia e implantodontia. "

```html
<!DOCTYPE html>
<html lang="pt-BR">
<head>
<meta charset="utf-8">
<title>Papelaria – Envelope Dr. Renato Valcourt</title>
<link rel="stylesheet" href="https://fonts.googleapis.com/css2?family=PT+Sans+Narrow:wght@400;700&family=Open+Sans:wght@400&display=swap">
<style>
  :root {
    --bg: #ecebe8;
    --teal: #4fd3cc;
    --teal-dark: #3cc3bc;
    --teal-faint: #46c9c2;
    --paper: #ffffff;
    --paper-shade: #eef1f1;
    --navy: #1f3f6e;
    --text-light: #ffffff;
  }
  * { margin: 0; padding: 0; box-sizing: border-box; }
  html, body { width: 1200px; height: 1200px; overflow: hidden; }
  body { background: var(--bg); position: relative; }

  .envelope { position: absolute; left: 144px; width: 936px; }

  /* front */
  .envelope--front { top: 139px; height: 444px; }
  .envelope__flap-top { position: absolute; inset: 0 0 auto 0; height: 60px; }
  .envelope__face {
    position: absolute; left: 0; right: 0; top: 53px; bottom: 0;
    background: radial-gradient(ellipse at 60% 30%, var(--paper) 40%, var(--paper-shade) 100%);
    box-shadow: 0 6px 14px rgba(0,0,0,.18);
  }
  .sender { position: absolute; left: 62px; top: 110px; }
  .sender__name {
    font-family: "PT Sans Narrow", sans-serif; font-weight: 700;
    font-size: 30px; color: var(--navy); line-height: 1; letter-spacing: .2px;
  }
  .sender__rule { height: 2px; width: 210px; background: var(--teal); margin: 5px 0 4px; }
  .sender__role {
    font-family: "Open Sans", sans-serif; font-size: 9px; letter-spacing: 3.4px;
    color: var(--navy);
  }
  .sender__reg {
    font-family: "Open Sans", sans-serif; font-size: 9px; color: var(--navy); margin-top: 3px;
  }

  /* back */
  .envelope--back {
    top: 605px; height: 432px; background: var(--teal);
    box-shadow: 0 6px 14px rgba(0,0,0,.18); overflow: hidden;
  }
  .envelope__flap { position: absolute; inset: 0 0 auto 0; height: 90px; }
  .envelope__mark {
    position: absolute; left: 730px; top: 175px; width: 230px; height: 230px;
    border-radius: 50%; background: var(--teal-faint);
  }
  .address {
    position: absolute; left: 12px; top: 306px;
    font-family: "Open Sans", sans-serif; font-size: 12px; line-height: 14.6px;
    color: var(--text-light); list-style: none;
  }
</style>
</head>
<body>
  <section class="envelope envelope--front" aria-label="Frente do envelope">
    <svg class="envelope__flap-top" viewBox="0 0 936 60" preserveAspectRatio="none" aria-hidden="true">
      <path d="M0 60 L0 18 Q0 0 40 0 L896 0 Q936 0 936 18 L936 60 Z" fill="var(--teal)"/>
    </svg>
    <div class="envelope__face">
      <div class="sender">
        <div class="sender__name">Dr. Renato Valcourt</div>
        <div class="sender__rule"></div>
        <div class="sender__role">Reabilitação Oral</div>
        <div class="sender__reg">CRO-RJ 48172</div>
      </div>
    </div>
  </section>

  <section class="envelope envelope--back" aria-label="Verso do envelope">
    <svg class="envelope__flap" viewBox="0 0 936 90" preserveAspectRatio="none" aria-hidden="true">
      <path d="M0 0 L936 0 L936 10 L870 80 Q862 88 850 88 L86 88 Q74 88 66 80 L0 10 Z" fill="var(--teal-dark)"/>
    </svg>
    <div class="envelope__mark" aria-hidden="true"></div>
    <ul class="address">
      <li>Conceição de Macabu - RJ</li>
      <li>Rua das Acácias, 58 - sala 04 Centro</li>
      <li>Tel: 22 2700-4811 Cep 28700-000</li>
      <li>Macaé - RJ - Clínica Aurora Saúde e Bem-Estar</li>
      <li>Rua Ernesto Lima, 310 - Imbetiba</li>
      <li>Tel: 22 2790-1234 / 2790-5678</li>
      <li>Cep 27900-100</li>
      <li>email: contato@renatovalcourt.com.br</li>
    </ul>
  </section>
</body>
</html>
```